HomePage Design for Bright Journeys - once-in-a-lifetime experiences for busy working people

Design a homepage for the Bright Journeys (www.brightjourneys-demo.com) website compatible with further web pages and the design briefing documents attached

BJ HomePage Design Brief
We are seeking website HomePage designs incorporating our new Logo and colour scheme, for Bright Journeys (www.brightjourneys-demo.com) to go with the site functionality and wireframe ideas attached.
The website HomePage design needs to
• Incorporate and be consistent with the BJ Logo and its colour scheme attached.
• Express the brand values of being inspirational, high quality, upscale, cultured, aspirational, and contemporary – even somewhat ‘hip’. Probably positioned somewhere between Mervyn Pask (Deluxe Travel) and Velvet Harbour (Hip Travel) – see https://www.mervynpask-demo.com and https://www.velvetharbour-demo.com .
• Be instantly recognisable and different from other travel websites and instantly communicate the nature of the brand proposition and target customer base.
• Appeal to our core 25-55 affluent businesspeople demographic
• Work in the UK, US/Canada and Australia/NZ and ultimately in mainland Europe.
• Use fonts and colours that are easily reproduced online and compatible with nearly all browsers.
• Be part of a responsive website design, that can be used both on Desktops and laptops but also with tablets and mobile ‘phones (hence content not too wide across the page)
• Feature the strapline ‘Bright Journeys in less than 7 Days’
• Work with the and wireframes and processes shown in the attached presentation – although intended as a guide only these features and processes all need to be incorporated into the HomePage.
• Make full use of high quality images and video to convey our brand proposition and products

Target Market(s)

25-55 affluent businesspeople

Industry/Entity Type

Travel Industry

Number of Pages Required

1 page

Font styles to use
Sans Serif

Colors
0455a3
00a88f

Requirements
Must have
• • Incorporate and be consistent with the BJ Logo and its colour scheme attached.
• • Express the brand values of being inspirational, high quality, upscale, cultured, aspirational, and contemporary – even somewhat ‘hip’. Probably positioned somewhere between Mervyn Pask (Deluxe Travel) and Velvet Harbour (Hip Travel) – see https://www.mervynpask-demo.com and https://www.velvetharbour-demo.com .
• • Be instantly recognisable and different from other travel websites and instantly communicate the nature of the brand proposition and target customer base.
• • Appeal to our core 25-55 affluent businesspeople demographic
• • Be part of a responsive website design, that can be used both on Desktops and laptops but also with tablets and mobile ‘phones (hence content not too wide across the page)
• • Feature the strapline ‘Bright Journeys in less than 7 Days’
• • Work with the and wireframes and processes shown in the attached presentation – although intended as a guide only these features and processes all need to be incorporated into the HomePage.
• • Make full use of high quality images and video to convey our brand proposition and products
• Colours as per Logo not as shown below
Nice to have
• • Work in the UK, US/Canada and Australia/NZ and ultimately in mainland Europe.
Should not have
• Must not be cheap or mass-market, nor excessively "stuffy or luxury-orientated"

```html
<!DOCTYPE html>
<html lang="en">
<head>
<meta charset="utf-8">
<title>Bright Journeys – Home</title>
<link rel="stylesheet" href="https://fonts.googleapis.com/css2?family=Roboto:wght@300;400;500;700&display=swap">
<style>
:root{
  --navy:#1e3163;
  --brand-blue:#0455a3;
  --brand-teal:#00a88f;
  --orange:#f26a10;
  --star:#e0262c;
  --text:#444;
  --muted:#888;
  --light-bg:#f4f4f4;
  --line:#e2e2e2;
  --dark:#2b3045;
}
*{box-sizing:border-box;margin:0;padding:0}
html,body{width:1200px;height:2862px;overflow:hidden}
body{font-family:"Roboto",Arial,sans-serif;color:var(--text);background:#fff;position:relative}
.container{width:864px;margin:0 auto;position:relative}

/* Header */
.site-header{height:95px;position:relative}
.site-header .container{height:95px}
.call{position:absolute;left:0;top:32px;font-size:17px;color:#222}
.mail{position:absolute;left:0;top:66px;font-size:10px;color:#222}
.logo{position:absolute;left:50%;top:20px;transform:translateX(-50%);text-align:center}
.logo-mark{width:46px;height:46px;border-radius:50%;background:var(--brand-teal);margin:0 auto 4px}
.logo-name{font-size:14px;font-weight:700;color:var(--navy);letter-spacing:1px;text-transform:uppercase;white-space:nowrap}
.header-tools{position:absolute;right:0;top:10px;text-align:right}
.login{font-size:9px;color:#222;margin-top:8px}
.socials{display:flex;gap:10px;justify-content:flex-end;margin-top:20px}
.socials span{width:11px;height:11px;border-radius:50%;background:#6b7483}
.main-nav{border-top:1px solid #d6d6d6;border-bottom:1px solid #d6d6d6;height:38px}
.main-nav ul{list-style:none;display:flex;justify-content:space-between;width:820px;margin:0 auto;height:38px;align-items:center}
.main-nav li{font-size:12px;color:#333;text-transform:uppercase}

/* Hero */
.hero{height:474px;position:relative;text-align:center;color:#fff}
.hero-image{position:absolute;inset:0;background:linear-gradient(180deg,#5d6b4a 0%,#6d8a6c 22%,#3fb6c4 48%,#12a7b6 70%,#0a6f86 100%)}
.hero-content{position:relative;padding-top:100px}
.hero h1{font-size:32px;font-weight:300;letter-spacing:.3px}
.hero h1 strong{font-weight:700}
.hero-sub{font-size:21px;font-weight:700;margin-top:40px;line-height:1.3}
.btn-primary{display:inline-block;background:var(--orange);color:#fff;font-size:17px;width:200px;height:36px;line-height:36px;margin-top:26px}

/* Intro */
.intro{background:var(--light-bg);height:725px;text-align:center;padding-top:46px}
.eyebrow{font-size:17px;letter-spacing:1.5px;color:#222;text-transform:uppercase}
.intro h2{font-size:22px;font-weight:700;color:var(--navy);margin-top:24px;text-transform:uppercase}
.intro p{font-size:13px;color:var(--muted);line-height:23px;width:780px;margin:12px auto 0}
.scroll-down{width:24px;height:24px;margin:22px auto 0;display:block}
.tiles{display:grid;grid-template-columns:repeat(4,200px);gap:24px 20px;width:860px;margin:33px auto 0}
.tile-image{height:137px}
.tile-label{font-size:11px;color:var(--muted);margin-top:8px;line-height:1.2}
.tile-label b{display:block;font-size:13px;font-weight:400;color:#333}

/* Video */
.video{height:448px;position:relative;text-align:center;color:#fff}
.video-image{position:absolute;inset:0;background:linear-gradient(180deg,#2e3133 0%,#4a5156 40%,#8a9aa2 62%,#2d2e2c 100%)}
.video-content{position:relative;padding-top:44px}
.video .lead{font-size:19px;font-weight:300}
.video .headline{font-size:28px;margin-top:10px}
.video .headline b{font-weight:700;text-transform:uppercase}
.video .note{font-size:22px;margin-top:4px}
.video .watch{font-size:13px;margin-top:16px}
.play{display:block;margin:4px auto 0}

/* Featured offers */
.offers{background:var(--light-bg);height:571px;padding-top:48px}
.section-title{text-align:center;font-size:18px;letter-spacing:1.5px;color:#222;text-transform:uppercase}
.cards{display:flex;gap:19px;width:846px;margin:34px auto 0}
.card{width:270px;height:404px;background:#fff;box-shadow:0 1px 3px rgba(0,0,0,.08)}
.card-image{height:166px}
.card-body{padding:18px 18px 0}
.card h3{font-size:17px;font-weight:700;color:var(--navy);text-transform:uppercase}
.card .meta{font-size:12px;color:var(--muted);margin-top:12px;display:flex;gap:6px;line-height:17px}
.card .meta svg{flex:none;margin-top:2px}
.price-table{display:grid;grid-template-columns:repeat(3,1fr);border-top:1px solid var(--line);border-bottom:1px solid var(--line);margin:14px -18px 0;padding:12px 18px;row-gap:10px;font-size:11px}
.price-table .label{color:#333;font-weight:500}
.price-table .value{color:#555}
.price-table .faint{color:#aaa}
.card-footer{display:flex;align-items:center;justify-content:space-between;padding:14px 18px}
.stars{display:flex;align-items:center;gap:2px;font-size:11px;color:var(--muted)}
.stars .reviews{margin-left:8px}

/* Newsletter */
.newsletter{height:137px;background:linear-gradient(100deg,var(--brand-teal) 0%,#028f97 45%,#0a6a8c 100%);text-align:center;color:#fff;padding-top:22px}
.newsletter h4{font-size:17px;font-weight:500;letter-spacing:1.5px;text-transform:uppercase}
.newsletter p{font-size:13px;margin-top:6px}
.signup{display:flex;gap:15px;justify-content:center;margin-top:12px;margin-left:-53px}
.field{width:296px;height:30px;border:1px solid rgba(255,255,255,.7);font-size:10px;text-align:left;padding:0 10px;line-height:28px}
.subscribe{width:122px;height:30px;background:var(--brand-blue);font-size:11px;letter-spacing:1px;line-height:30px;text-transform:uppercase}

/* Share */
.share{height:124px;text-align:center;padding-top:26px}
.share h4{font-size:18px;font-weight:400;letter-spacing:1.5px;text-transform:uppercase;color:#222}
.share-links{display:flex;gap:18px;justify-content:center;margin:18px auto 0;width:600px;font-size:11px;color:var(--muted);background:linear-gradient(90deg,transparent,#f1f1f1 20%,#f1f1f1 80%,transparent);height:26px;align-items:center}
.share-links span::before{content:"";display:inline-block;width:8px;height:8px;border-radius:50%;background:#666;margin-right:4px}

/* Footer */
.footer-links{height:156px;position:relative}
.footer-col{position:absolute;top:20px}
.footer-col h5{font-size:13px;font-weight:400;letter-spacing:1.5px;color:#222;text-transform:uppercase}
.footer-col h5::after{content:"";display:block;width:30px;height:1px;background:#222;margin-top:6px}
.footer-col ul{list-style:none;margin-top:8px}
.footer-col li{font-size:10px;color:var(--muted);line-height:18px}
.mission{height:50px;background:#ececec;text-align:center;font-size:15px;line-height:50px;color:#333}
.copyright{height:42px;background:var(--dark);color:#ccc;font-size:10px;text-align:center;line-height:42px}
</style>
</head>
<body>

<header class="site-header">
  <div class="container">
    <div class="call">CALL: 020 555 0147</div>
    <div class="mail">MAIL: hello@brightjourneys-demo.com</div>
    <div class="logo">
      <div class="logo-mark"></div>
      <div class="logo-name">Bright Journeys</div>
    </div>
    <div class="header-tools">
      <svg width="14" height="14" viewBox="0 0 14 14"><circle cx="5.5" cy="5.5" r="4.2" fill="none" stroke="#222" stroke-width="2"/><line x1="8.6" y1="8.6" x2="13" y2="13" stroke="#222" stroke-width="2.2"/></svg>
      <div class="login">&#9658; LOG-IN</div>
      <div class="socials"><span></span><span></span><span></span><span></span><span></span></div>
    </div>
  </div>
</header>

<nav class="main-nav">
  <ul>
    <li>Destinations &#709;</li>
    <li>Experiences &#709;</li>
    <li>Trips by Month &#709;</li>
    <li>Topical Now</li>
    <li>Tailored</li>
    <li>Pioneers Club</li>
    <li>Blogs &amp; Reviews</li>
  </ul>
</nav>

<section class="hero">
  <div class="hero-image" role="img" aria-label="Turquoise bay beneath limestone cliffs with a wooden longtail boat in the foreground"></div>
  <div class="hero-content">
    <h1>Once-in-a-Lifetime Experiences in Less Than <strong>7 Days</strong></h1>
    <div class="hero-sub">Extraordinary &amp;<br>Secret Places Of The World!</div>
    <a class="btn-primary">Look, Book &amp; Go</a>
  </div>
</section>

<section class="intro">
  <div class="eyebrow">Too Busy to Research and Book a Trip?</div>
  <h2>Choose Our Pre-Packaged Trips with an Easy 'Look and Book' Concept</h2>
  <p>Maximum Experiences in the Minimum Time Necessary to Enjoy. Can be Taken in a Weekend, Long-Weekend, or for Further Away or More Involved Experiences, up to One Working Week.</p>
  <svg class="scroll-down" viewBox="0 0 24 24"><circle cx="12" cy="12" r="11" fill="none" stroke="#555" stroke-width="1"/><polyline points="8,10 12,14 16,10" fill="none" stroke="#555" stroke-width="1.3"/></svg>
  <div class="tiles">
    <div class="tile"><div class="tile-image" role="img" aria-label="Safari wildlife on grassland" style="background:linear-gradient(180deg,#6f8a3c,#8a7a45)"></div><div class="tile-label">Wonders<b>of Wildlife</b></div></div>
    <div class="tile"><div class="tile-image" role="img" aria-label="Colourful powder festival crowd" style="background:linear-gradient(135deg,#d9462f,#e4a23a,#8c3ca0)"></div><div class="tile-label">World's<b>Greatest Festivals</b></div></div>
    <div class="tile"><div class="tile-image" role="img" aria-label="White-water kayaking" style="background:linear-gradient(180deg,#4f7ea3,#b9cfdc)"></div><div class="tile-label">Must Do<b>Activities</b></div></div>
    <div class="tile"><div class="tile-image" role="img" aria-label="Hot air balloons rising at an annual event" style="background:linear-gradient(180deg,#9fc3e2,#d65a3a 70%,#5c7a4a)"></div><div class="tile-label">Unique<b>Annual Events</b></div></div>
    <div class="tile"><div class="tile-image" role="img" aria-label="Hidden cave with green lagoon" style="background:linear-gradient(180deg,#1c3a3a,#2f7a6a,#0e2a2c)"></div><div class="tile-label">Extraordinary &amp;<b>Secret Places</b></div></div>
    <div class="tile"><div class="tile-image" role="img" aria-label="Dancers performing on stage" style="background:linear-gradient(135deg,#3a0c14,#d8336a,#f07aa8)"></div><div class="tile-label">Unforgettable<b>Performances</b></div></div>
    <div class="tile"><div class="tile-image" role="img" aria-label="Climbers on a rocky mountain ridge" style="background:linear-gradient(180deg,#a7b6c8,#5a5f66)"></div><div class="tile-label">Spectacular Hiking,<b>Climbing &amp; Walking</b></div></div>
    <div class="tile"><div class="tile-image" role="img" aria-label="Colourful hilltop palace" style="background:linear-gradient(180deg,#6aa0d8,#e2c24a 55%,#8c4a3a)"></div><div class="tile-label">Private Castles,<b>Chateaux &amp; Paradors</b></div></div>
  </div>
</section>

<section class="video">
  <div class="video-image" role="img" aria-label="Hikers crossing rocks beside a mountain lake with snowy slopes"></div>
  <div class="video-content">
    <div class="lead">Have Limited Time to Research and Book a Trip?</div>
    <div class="headline"><b>Bright Journeys</b> have Designed Just for You.</div>
    <div class="note">All Experiences Can be Completed in Less than <b>7 DAYS</b>.</div>
    <div class="watch">Watch Video</div>
    <svg class="play" width="86" height="86" viewBox="0 0 86 86"><circle cx="43" cy="43" r="40" fill="rgba(0,0,0,.15)" stroke="#fff" stroke-width="3"/><polygon points="35,27 62,43 35,59" fill="#fff"/></svg>
  </div>
</section>

<section class="offers">
  <div class="section-title">Featured Offers</div>
  <div class="cards">
    <article class="card">
      <div class="card-image" role="img" aria-label="Kayaker paddling through splashing water" style="background:linear-gradient(180deg,#8a8070,#c23a3a 75%,#6e6a62)"></div>
      <div class="card-body">
        <h3>Vestibulum in Imperdiet</h3>
        <div class="meta"><svg width="9" height="12" viewBox="0 0 9 12"><path d="M4.5 0C2 0 0 2 0 4.5 0 8 4.5 12 4.5 12S9 8 9 4.5C9 2 7 0 4.5 0z" fill="var(--star)"/><circle cx="4.5" cy="4.5" r="1.6" fill="#fff"/></svg>Latin America, North America, Mexico, Baja</div>
        <div class="meta"><svg width="11" height="11" viewBox="0 0 11 11"><circle cx="5.5" cy="5.5" r="4.5" fill="none" stroke="var(--star)" stroke-width="1.5"/><polyline points="5.5,3 5.5,5.5 7.5,6.5" fill="none" stroke="var(--star)" stroke-width="1.2"/></svg>6 to 7 days</div>
        <div class="price-table">
          <span class="label">&#9679; Adult:</span><span class="label">&#9679; Child:</span><span class="label">&#9679; Min. Age:</span>
          <span class="value">£ 1234</span><span class="value">£ 1000</span><span class="faint">11-12</span>
        </div>
      </div>
      <div class="card-footer">
        <div class="stars"><svg width="70" height="12" viewBox="0 0 70 12"><g fill="var(--star)"><polygon points="6,0 7.8,4 12,4.4 8.8,7.2 9.8,11.5 6,9.2 2.2,11.5 3.2,7.2 0,4.4 4.2,4"/><polygon transform="translate(14)" points="6,0 7.8,4 12,4.4 8.8,7.2 9.8,11.5 6,9.2 2.2,11.5 3.2,7.2 0,4.4 4.2,4"/><polygon transform="translate(28)" points="6,0 7.8,4 12,4.4 8.8,7.2 9.8,11.5 6,9.2 2.2,11.5 3.2,7.2 0,4.4 4.2,4"/><polygon transform="translate(42)" points="6,0 7.8,4 12,4.4 8.8,7.2 9.8,11.5 6,9.2 2.2,11.5 3.2,7.2 0,4.4 4.2,4"/></g><polygon fill="#ccc" transform="translate(56)" points="6,0 7.8,4 12,4.4 8.8,7.2 9.8,11.5 6,9.2 2.2,11.5 3.2,7.2 0,4.4 4.2,4"/></svg><span class="reviews">(3 reviews)</span></div>
        <svg width="11" height="12" viewBox="0 0 11 12"><circle cx="9" cy="2" r="2" fill="#333"/><circle cx="2" cy="6" r="2" fill="#333"/><circle cx="9" cy="10" r="2" fill="#333"/><path d="M9 2L2 6L9 10" fill="none" stroke="#333"/></svg>
      </div>
    </article>
    <article class="card">
      <div class="card-image" role="img" aria-label="Hikers resting above a desert canyon" style="background:linear-gradient(180deg,#b89a70,#d8c7a8 55%,#8a6e4a)"></div>
      <div class="card-body">
        <h3>Vestibulum in Imperdiet</h3>
        <div class="meta"><svg width="9" height="12" viewBox="0 0 9 12"><path d="M4.5 0C2 0 0 2 0 4.5 0 8 4.5 12 4.5 12S9 8 9 4.5C9 2 7 0 4.5 0z" fill="var(--star)"/><circle cx="4.5" cy="4.5" r="1.6" fill="#fff"/></svg>Latin America, North America, Mexico, Baja</div>
        <div class="meta"><svg width="11" height="11" viewBox="0 0 11 11"><circle cx="5.5" cy="5.5" r="4.5" fill="none" stroke="var(--star)" stroke-width="1.5"/><polyline points="5.5,3 5.5,5.5 7.5,6.5" fill="none" stroke="var(--star)" stroke-width="1.2"/></svg>6 to 7 days</div>
        <div class="price-table">
          <span class="label">&#9679; Adult:</span><span class="label">&#9679; Child:</span><span class="label">&#9679; Min. Age:</span>
          <span class="value">£ 1234</span><span class="value">£ 1000</span><span class="faint">11-12</span>
        </div>
      </div>
      <div class="card-footer">
        <div class="stars"><svg width="70" height="12" viewBox="0 0 70 12"><g fill="var(--star)"><polygon points="6,0 7.8,4 12,4.4 8.8,7.2 9.8,11.5 6,9.2 2.2,11.5 3.2,7.2 0,4.4 4.2,4"/><polygon transform="translate(14)" points="6,0 7.8,4 12,4.4 8.8,7.2 9.8,11.5 6,9.2 2.2,11.5 3.2,7.2 0,4.4 4.2,4"/><polygon transform="translate(28)" points="6,0 7.8,4 12,4.4 8.8,7.2 9.8,11.5 6,9.2 2.2,11.5 3.2,7.2 0,4.4 4.2,4"/><polygon transform="translate(42)" points="6,0 7.8,4 12,4.4 8.8,7.2 9.8,11.5 6,9.2 2.2,11.5 3.2,7.2 0,4.4 4.2,4"/></g><polygon fill="#ccc" transform="translate(56)" points="6,0 7.8,4 12,4.4 8.8,7.2 9.8,11.5 6,9.2 2.2,11.5 3.2,7.2 0,4.4 4.2,4"/></svg><span class="reviews">(3 reviews)</span></div>
        <svg width="11" height="12" viewBox="0 0 11 12"><circle cx="9" cy="2" r="2" fill="#333"/><circle cx="2" cy="6" r="2" fill="#333"/><circle cx="9" cy="10" r="2" fill="#333"/><path d="M9 2L2 6L9 10" fill="none" stroke="#333"/></svg>
      </div>
    </article>
    <article class="card">
      <div class="card-image" role="img" aria-label="Reed boats and huts on a highland lake" style="background:linear-gradient(180deg,#8ab0cc,#b89a5a 55%,#6a5a30)"></div>
      <div class="card-body">
        <h3>Vestibulum in Imperdiet</h3>
        <div class="meta"><svg width="9" height="12" viewBox="0 0 9 12"><path d="M4.5 0C2 0 0 2 0 4.5 0 8 4.5 12 4.5 12S9 8 9 4.5C9 2 7 0 4.5 0z" fill="var(--star)"/><circle cx="4.5" cy="4.5" r="1.6" fill="#fff"/></svg>Latin America, North America, Mexico, Baja</div>
        <div class="meta"><svg width="11" height="11" viewBox="0 0 11 11"><circle cx="5.5" cy="5.5" r="4.5" fill="none" stroke="var(--star)" stroke-width="1.5"/><polyline points="5.5,3 5.5,5.5 7.5,6.5" fill="none" stroke="var(--star)" stroke-width="1.2"/></svg>6 to 7 days</div>
        <div class="price-table">
          <span class="label">&#9679; Adult:</span><span class="label">&#9679; Child:</span><span class="label">&#9679; Min. Age:</span>
          <span class="value">£ 1234</span><span class="value">£ 1000</span><span class="value">NA</span>
        </div>
      </div>
      <div class="card-footer">
        <div class="stars"><svg width="70" height="12" viewBox="0 0 70 12"><g fill="var(--star)"><polygon points="6,0 7.8,4 12,4.4 8.8,7.2 9.8,11.5 6,9.2 2.2,11.5 3.2,7.2 0,4.4 4.2,4"/><polygon transform="translate(14)" points="6,0 7.8,4 12,4.4 8.8,7.2 9.8,11.5 6,9.2 2.2,11.5 3.2,7.2 0,4.4 4.2,4"/><polygon transform="translate(28)" points="6,0 7.8,4 12,4.4 8.8,7.2 9.8,11.5 6,9.2 2.2,11.5 3.2,7.2 0,4.4 4.2,4"/><polygon transform="translate(42)" points="6,0 7.8,4 12,4.4 8.8,7.2 9.8,11.5 6,9.2 2.2,11.5 3.2,7.2 0,4.4 4.2,4"/></g><polygon fill="#ccc" transform="translate(56)" points="6,0 7.8,4 12,4.4 8.8,7.2 9.8,11.5 6,9.2 2.2,11.5 3.2,7.2 0,4.4 4.2,4"/></svg><span class="reviews">(3 reviews)</span></div>
        <svg width="11" height="12" viewBox="0 0 11 12"><circle cx="9" cy="2" r="2" fill="#333"/><circle cx="2" cy="6" r="2" fill="#333"/><circle cx="9" cy="10" r="2" fill="#333"/><path d="M9 2L2 6L9 10" fill="none" stroke="#333"/></svg>
      </div>
    </article>
  </div>
</section>

<section class="newsletter">
  <h4>Signup for our Newsletter</h4>
  <p>Receive news and offers from BJ</p>
  <div class="signup">
    <div class="field">Your Full Name</div>
    <div class="field">Email Address</div>
    <div class="subscribe">Subscribe</div>
  </div>
</section>

<section class="share">
  <h4>Share Us</h4>
  <div class="share-links"><span>Facenote</span><span>Chirper</span><span>Pinboard</span><span>Snapgram</span><span>Viewtube</span></div>
</section>

<footer>
  <div class="footer-links container">
    <div class="footer-col" style="left:0"><h5>Quick Links</h5><ul><li>Home</li><li>About</li><li>Contacts Us</li></ul></div>
    <div class="footer-col" style="left:183px"><h5>Resources</h5><ul><li>Our Partner</li><li>Careers with BJ</li><li>Press Room</li></ul></div>
    <div class="footer-col" style="left:401px"><h5>Support</h5><ul><li>Travel Advice</li><li>Financial Protection</li><li>Travel Insurance</li><li>FAQs</li><li>Contacts Us</li></ul></div>
    <div class="footer-col" style="left:553px"><h5>Booking</h5><ul><li>Booking Conditions</li><li>Group Bookings</li><li>Tailor-Made &amp; Extra Nights</li><li>Booking Flights</li></ul></div>
    <div class="footer-col" style="left:721px"><h5>Information</h5><ul><li>Visas</li><li>Terms of Use</li><li>Privacy &amp; Cookies</li></ul></div>
  </div>
  <div class="mission">BJ Protecting wildlife &amp; animals,and supporting local communities</div>
  <div class="copyright">Copyright 2017 www.brightjourneys-demo.com All Rights Reserved.</div>
</footer>

</body>
</html>
```